Business Card for By Karel Voss

Looking to have a business card designed for my lifestyle and fitness company. My company offers personal training, online programming and nutrition advice based out of London, United Kingdom.

I'd like to see modern, sleek designs, focusing on black, matte black or matte grey. Design doesn't need to be overly descriptive as this will also be used as a personal business card. I've included my logo.

Please note that my company is no longer called "Fitness by Karel Voss" but instead "By Karel Voss", this is because of my other ventures. Therefore please don't use the "fitness by karel voss" text.

information about my company can be found at www.bykarelvoss.com

Company is also based out of London (United Kingdom) & Sydney (Australia) this could be reflected on the card.

Industry/Entity Type

Business

Contact Information for Business Card

Karel Voss
+44 7382 615027
karel@bykarelvoss.com
www.bykarelvoss.com

Font styles to use
Sans Serif

Requirements
Must have
• All contact details and inclusion of my logo.

```html
<!DOCTYPE html>
<html lang="en">
<head>
<meta charset="utf-8">
<title>By Karel Voss — Business Card</title>
<link rel="stylesheet" href="https://fonts.googleapis.com/css2?family=Roboto:wght@400;500;700&display=swap">
<style>
  :root {
    --backdrop: #3a322e;
    --card: #1c1f21;
    --card-edge: #111315;
    --ink: #f2f2f2;
    --ink-soft: #9a9c9e;
    --rule: #d8d8d8;
  }
  * { box-sizing: border-box; margin: 0; padding: 0; }
  html, body { width: 1200px; height: 769px; overflow: hidden; }
  body {
    background: var(--backdrop);
    font-family: "Roboto", Arial, sans-serif;
    position: relative;
  }
  .card {
    position: absolute;
    width: 520px;
    height: 298px;
    background: var(--card);
    border-radius: 3px;
    box-shadow: 0 3px 0 var(--card-edge), 0 12px 30px rgba(0,0,0,.45);
    overflow: hidden;
  }
  .card--front { left: 60px; top: 110px; }
  .card--back { left: 620px; top: 360px; }

  /* front */
  .front-mark {
    position: absolute;
    left: 0; right: 0; top: 96px;
    display: flex; align-items: center; justify-content: center; gap: 12px;
    color: var(--ink-soft);
    font-weight: 700;
    font-size: 30px;
    letter-spacing: 1px;
    text-transform: uppercase;
  }
  .front-mark .dot {
    width: 16px; height: 16px; border-radius: 50%; background: var(--ink-soft);
  }
  .front-url {
    position: absolute;
    left: 0; right: 0; top: 196px;
    text-align: center;
    color: var(--ink-soft);
    font-size: 13px;
    letter-spacing: 4px;
  }

  /* back */
  .holder {
    position: absolute;
    left: 36px; top: 92px;
    color: var(--ink);
    font-weight: 500;
    font-size: 16px;
    text-transform: uppercase;
  }
  .divider {
    position: absolute;
    left: 36px; right: 36px;
    height: 1px;
    background: var(--rule);
  }
  .divider--top { top: 118px; }
  .divider--bottom { top: 262px; }
  .contacts {
    position: absolute;
    left: 30px; top: 128px;
    list-style: none;
    color: var(--ink);
    font-size: 13px;
    line-height: 20px;
  }
  .contacts li { display: flex; align-items: center; gap: 8px; }
  .contacts svg { width: 11px; height: 11px; flex: none; }
  .back-mark {
    position: absolute;
    right: 36px; top: 150px;
    display: flex; align-items: center; gap: 8px;
    color: var(--ink);
    font-weight: 700;
    font-size: 20px;
    text-transform: uppercase;
  }
  .back-mark .dot {
    width: 12px; height: 12px; border-radius: 50%; background: var(--ink);
  }
</style>
</head>
<body>
  <section class="card card--front" aria-label="Card front">
    <div class="front-mark"><span class="dot"></span><span>By Karel Voss</span></div>
    <p class="front-url">www.bykarelvoss.com</p>
  </section>

  <section class="card card--back" aria-label="Card back">
    <h1 class="holder">Karel Voss</h1>
    <div class="divider divider--top"></div>
    <ul class="contacts">
      <li>
        <svg viewBox="0 0 12 12" fill="none" stroke="currentColor" stroke-width="1.2"><rect x="3" y="0.8" width="6" height="10.4" rx="1"/><line x1="5" y1="9.4" x2="7" y2="9.4"/></svg>
        +44 7382 615027
      </li>
      <li>
        <svg viewBox="0 0 12 12" fill="none" stroke="currentColor" stroke-width="1.2"><rect x="0.8" y="2.5" width="10.4" height="7" rx="0.5"/><polyline points="1,3 6,7 11,3"/></svg>
        karel@bykarelvoss.com
      </li>
      <li>
        <svg viewBox="0 0 12 12" fill="none" stroke="currentColor" stroke-width="1.1"><circle cx="6" cy="6" r="5"/><ellipse cx="6" cy="6" rx="2.2" ry="5"/><line x1="1" y1="6" x2="11" y2="6"/></svg>
        www.bykarelvoss.com
      </li>
    </ul>
    <div class="back-mark"><span class="dot"></span><span>By Karel Voss</span></div>
    <div class="divider divider--bottom"></div>
  </section>
</body>
</html>
```